Vorna Fleet business card

I am needing a business card that at a glance shows all the services that we provide emphasizing some more than others. We are a Fleet and Compliance management company as well as a software company. We provide outsourced solutions for KPX compliance and HR services via our own software.
In addition, we do
drug testing
GPS
Cameras
Electronic DVIRS
ELD's

Target Market(s)

Transportation company owners

Industry/Entity Type

Transportation supplier

Contact Information for Business Card

the card should inform potential customers what we do

Other font styles liked:
• I have added brand guidelines. See attached

Requirements
Must have
• See description
Should not have
• Colors outside my brand guide. See attached

```html
<!DOCTYPE html>
<html lang="en">
<head>
<meta charset="utf-8">
<title>Vorna Fleet — Business Card</title>
<link rel="stylesheet" href="https://fonts.googleapis.com/css2?family=Michroma&family=Roboto:wght@400;500&display=swap">
<style>
  :root {
    --ink: #0d0d0d;
    --brand-red: #e8262b;
    --paper: #ffffff;
    --backdrop: #d9d9db;
    --muted: #1c1c1c;
  }
  * { box-sizing: border-box; margin: 0; padding: 0; }
  html, body { width: 1200px; height: 900px; overflow: hidden; }
  body {
    background: var(--backdrop);
    font-family: "Roboto", Arial, sans-serif;
    position: relative;
  }
  .card {
    position: absolute;
    left: 250px;
    width: 700px;
    height: 400px;
    background: var(--paper);
    overflow: hidden;
    box-shadow: 0 8px 24px rgba(0,0,0,.18);
  }
  .card--back { top: 35px; }
  .card--front { top: 465px; }
  .card__shapes { position: absolute; inset: 0; width: 700px; height: 400px; }

  .wordmark {
    position: absolute;
    display: flex;
    align-items: center;
    gap: 14px;
    font-family: "Michroma", "Arial Black", sans-serif;
    color: var(--ink);
    letter-spacing: 3px;
    white-space: nowrap;
  }
  .wordmark__square { background: var(--brand-red); flex: none; }
  .card--back .wordmark { left: 40px; top: 312px; font-size: 30px; }
  .card--back .wordmark__square { width: 22px; height: 22px; }
  .card--front .wordmark { left: 40px; top: 86px; font-size: 40px; line-height: 1.15; letter-spacing: 6px; }
  .card--front .wordmark__square { width: 30px; height: 30px; }

  .services {
    position: absolute;
    right: 108px;
    top: 30px;
    text-align: right;
    font-family: "Michroma", sans-serif;
    text-transform: uppercase;
  }
  .services__headline {
    color: var(--brand-red);
    font-size: 12.5px;
    line-height: 1.45;
    letter-spacing: 1px;
    margin-bottom: 10px;
  }
  .services__list { list-style: none; }
  .services__item {
    display: flex;
    justify-content: flex-end;
    align-items: center;
    gap: 10px;
    color: #fff;
    font-size: 12px;
    letter-spacing: 1px;
    line-height: 24px;
  }
  .services__icon { width: 16px; height: 16px; flex: none; }

  .identity {
    position: absolute;
    left: 405px;
    top: 72px;
    width: 250px;
    text-align: center;
    font-family: "Michroma", sans-serif;
    text-transform: uppercase;
  }
  .identity__name { color: #fff; font-size: 19px; letter-spacing: 2px; }
  .identity__title { color: var(--brand-red); font-size: 10px; letter-spacing: 1px; margin-top: 4px; }

  .address {
    position: absolute;
    left: 452px;
    top: 282px;
    display: flex;
    gap: 8px;
    font-size: 15px;
    line-height: 1.3;
    color: var(--muted);
  }
  .address__pin { width: 14px; height: 18px; margin-top: 6px; flex: none; }

  .contacts {
    position: absolute;
    left: 70px;
    top: 222px;
    list-style: none;
  }
  .contacts__item {
    display: flex;
    align-items: center;
    gap: 12px;
    font-size: 17px;
    letter-spacing: 1px;
    line-height: 26px;
    color: var(--muted);
  }
  .contacts__icon { width: 15px; height: 15px; flex: none; }
</style>
</head>
<body>

<!-- Reverse side: services -->
<section class="card card--back">
  <svg class="card__shapes" viewBox="0 0 700 400" aria-hidden="true">
    <circle cx="470" cy="-20" r="250" fill="var(--ink)"/>
    <path d="M200 70 A285 285 0 0 0 700 148" fill="none" stroke="var(--brand-red)" stroke-width="2"/>
    <circle cx="200" cy="70" r="8" fill="var(--brand-red)"/>
    <path d="M151 0 A320 320 0 0 0 600 272" fill="none" stroke="var(--ink)" stroke-width="2"/>
    <circle cx="600" cy="272" r="8" fill="var(--ink)"/>
  </svg>

  <div class="services">
    <p class="services__headline">We provide outsourced<br>solutions for KPX compliance<br>and HR services</p>
    <ul class="services__list">
      <li class="services__item">Drug testing
        <svg class="services__icon" viewBox="0 0 16 16" fill="none" stroke="var(--brand-red)" stroke-width="1.3"><path d="M3 13 L11 5 M9 3 L13 7 M4 10 L6 12 M1 15 L3 13"/></svg></li>
      <li class="services__item">GPS
        <svg class="services__icon" viewBox="0 0 16 16" fill="none" stroke="var(--brand-red)" stroke-width="1.3"><path d="M8 15 C4 10 3 8 3 6 A5 5 0 0 1 13 6 C13 8 12 10 8 15Z"/><circle cx="8" cy="6" r="1.8"/></svg></li>
      <li class="services__item">Cameras
        <svg class="services__icon" viewBox="0 0 16 16" fill="none" stroke="var(--brand-red)" stroke-width="1.3"><rect x="1" y="5" width="10" height="7" rx="1"/><path d="M11 7 L15 5 L15 12 L11 10"/></svg></li>
      <li class="services__item">Electronic DVIRs
        <svg class="services__icon" viewBox="0 0 16 16" fill="none" stroke="var(--brand-red)" stroke-width="1.3"><rect x="3" y="1.5" width="10" height="13" rx="1"/><path d="M5.5 6 L10.5 6 M5.5 9 L10.5 9 M5.5 12 L8.5 12"/></svg></li>
      <li class="services__item">ELD's
        <svg class="services__icon" viewBox="0 0 16 16" fill="none" stroke="var(--brand-red)" stroke-width="1.3"><circle cx="8" cy="8" r="6.5"/><path d="M8 4 L8 8 L11 10"/></svg></li>
    </ul>
  </div>

  <div class="wordmark"><span class="wordmark__square"></span><span class="wordmark__text">VORNA FLEET</span></div>
</section>

<!-- Front side: contact -->
<section class="card card--front">
  <svg class="card__shapes" viewBox="0 0 700 400" aria-hidden="true">
    <circle cx="530" cy="60" r="145" fill="var(--ink)"/>
    <path d="M435 201 A170 170 0 0 0 700 60" fill="none" stroke="var(--brand-red)" stroke-width="2"/>
    <circle cx="435" cy="201" r="7" fill="var(--brand-red)"/>
    <path d="M339 0 A200 200 0 0 0 610 243" fill="none" stroke="var(--ink)" stroke-width="2"/>
    <circle cx="610" cy="243" r="7" fill="var(--ink)"/>
    <circle cx="30" cy="420" r="95" fill="var(--ink)"/>
  </svg>

  <div class="identity">
    <p class="identity__name">Dana Mercer</p>
    <p class="identity__title">Managing Director</p>
  </div>

  <div class="wordmark"><span class="wordmark__square"></span><span class="wordmark__text">VORNA<br>FLEET</span></div>

  <div class="address">
    <svg class="address__pin" viewBox="0 0 14 18"><path d="M7 17 C2.5 11 1 9 1 6.5 A6 6 0 0 1 13 6.5 C13 9 11.5 11 7 17Z" fill="var(--brand-red)"/><circle cx="7" cy="6.5" r="2.3" fill="#fff"/></svg>
    <p>Put your address here<br>Street, City, Country</p>
  </div>

  <ul class="contacts">
    <li class="contacts__item">
      <svg class="contacts__icon" viewBox="0 0 16 16"><path d="M4 1 L6.5 4.5 L5 6.5 C6 8.5 7.5 10 9.5 11 L11.5 9.5 L15 12 L13.5 14.5 C7 14.5 1.5 9 1.5 2.5Z" fill="var(--brand-red)"/></svg>555.014.2280</li>
    <li class="contacts__item">
      <svg class="contacts__icon" viewBox="0 0 16 16" fill="var(--brand-red)"><rect x="4" y="1" width="8" height="4"/><rect x="1" y="6" width="14" height="6" rx="1"/><rect x="4" y="10" width="8" height="5" fill="#fff" stroke="var(--brand-red)" stroke-width="1.2"/></svg>555.014.2281</li>
    <li class="contacts__item">
      <svg class="contacts__icon" viewBox="0 0 16 16"><rect x="1" y="3" width="14" height="10" fill="var(--brand-red)"/><path d="M1 3 L8 9 L15 3" fill="none" stroke="#fff" stroke-width="1.2"/></svg>dana@vornafleet.com</li>
    <li class="contacts__item">
      <svg class="contacts__icon" viewBox="0 0 16 16" fill="none" stroke="var(--brand-red)" stroke-width="1.2"><circle cx="8" cy="8" r="6.5"/><ellipse cx="8" cy="8" rx="3" ry="6.5"/><path d="M1.5 8 H14.5 M2.5 4.5 H13.5 M2.5 11.5 H13.5"/></svg>www.vornafleet.com</li>
  </ul>
</section>

</body>
</html>
```